Business Card Design Project - Brantwell Media

We need a new business card that fits with our new logo. We are a social media agency and consultancy operating in China. We want a fresh and strong business card. Our cards need to be two-sided as we have both English and Chinese language names and addresses on the card, but as with our current business card this does not need to be a mirror-image. Our thoughts go out to a white card on the front where the logo/name is and then using the logo colours for different coloured back-grounds. i.e that the back of the biz card works with the four different colours in the logo.

Attached is the new logo, and also a copy of our old business cards.

Target Market(s)

CEO's, CMO's. media and advertising professionals

Industry/Entity Type

Business

Requirements
Must have
• inclusion of both Chinese and English language
Nice to have
• four different colored versions of the back of the biz card. Our logo has four colors and each of these colors we would like to have a version of.

```html
<!DOCTYPE html>
<html lang="en">
<head>
<meta charset="utf-8">
<title>Brantwell Media – Business Card</title>
<link rel="stylesheet" href="https://fonts.googleapis.com/css2?family=Arimo:wght@400;700&family=Saira+Semi+Condensed:wght@400&family=Noto+Sans+SC:wght@400;700&display=swap">
<style>
  :root {
    --backdrop: #dcdcdc;
    --card: #ffffff;
    --ink: #231f20;
    --grey: #7a7a7a;
    --orange: #f15a24;
    --purple: #6f2c91;
    --magenta: #e6007e;
    --green: #8dc63f;
    --on-colour: #ffffff;
  }
  * { margin: 0; padding: 0; box-sizing: border-box; }
  html, body { width: 1200px; height: 724px; overflow: hidden; }
  body {
    background: var(--backdrop);
    position: relative;
    font-family: "Arimo", Arial, sans-serif;
    color: var(--ink);
  }
  .card {
    position: absolute;
    top: 186px;
    width: 462px;
    height: 277px;
    overflow: hidden;
  }
  .card--front { left: 103px; background: var(--card); }
  .card--back { left: 607px; background: var(--purple); color: var(--on-colour); }

  /* Front */
  .brand {
    position: absolute;
    left: 17px;
    top: 82px;
  }
  .brand__row {
    display: flex;
    align-items: center;
    gap: 10px;
  }
  .brand__name {
    font-weight: 700;
    font-size: 40px;
    letter-spacing: -1px;
    line-height: 1;
    color: var(--ink);
  }
  .brand__square {
    width: 12px;
    height: 12px;
    background: var(--purple);
  }
  .brand__name-cn {
    margin-top: 10px;
    font-family: "Noto Sans SC", sans-serif;
    font-size: 18px;
    letter-spacing: 4px;
    color: var(--ink);
  }
  .website {
    position: absolute;
    left: 17px;
    bottom: 18px;
    font-size: 16px;
    color: var(--ink);
  }

  /* Back */
  .brand-vertical {
    position: absolute;
    left: 0;
    top: 0;
    width: 52px;
    height: 277px;
    display: flex;
    align-items: center;
    justify-content: center;
  }
  .brand-vertical__name {
    transform: rotate(90deg);
    white-space: nowrap;
    font-weight: 700;
    font-size: 34px;
    letter-spacing: -1px;
    color: var(--on-colour);
  }
  .contact {
    position: absolute;
    left: 141px;
    top: 40px;
    right: 12px;
  }
  .contact__name {
    font-size: 24px;
    font-weight: 400;
    line-height: 1;
    color: var(--on-colour);
  }
  .contact__name-cn {
    font-family: "Noto Sans SC", sans-serif;
    font-size: 18px;
    margin-left: 8px;
  }
  .contact__role {
    margin-top: 6px;
    font-family: "Saira Semi Condensed", Arial, sans-serif;
    font-size: 16px;
    letter-spacing: 0.3px;
    line-height: 1.2;
  }
  .contact__role-cn {
    font-family: "Noto Sans SC", sans-serif;
    font-size: 13px;
    margin-left: 6px;
  }
  .contact__details {
    margin-top: 20px;
    font-family: "Saira Semi Condensed", Arial, sans-serif;
    font-size: 14.4px;
    line-height: 17.4px;
    font-style: normal;
    letter-spacing: 0.2px;
  }
  .contact__details-cn {
    margin-top: 8px;
    font-family: "Noto Sans SC", sans-serif;
    font-size: 12.5px;
    line-height: 18px;
    font-style: normal;
  }
</style>
</head>
<body>
  <section class="card card--front" aria-label="Card front">
    <div class="brand">
      <div class="brand__row">
        <span class="brand__name">Brantwell Media</span>
        <span class="brand__square"></span>
      </div>
      <p class="brand__name-cn" lang="zh">博朗威传媒</p>
    </div>
    <p class="website">www.brantwellchina.cn</p>
  </section>

  <section class="card card--back" aria-label="Card back">
    <div class="brand-vertical">
      <span class="brand-vertical__name">Brantwell</span>
    </div>
    <div class="contact">
      <h1 class="contact__name">Owen Hartley<span class="contact__name-cn" lang="zh">何欧文</span></h1>
      <p class="contact__role">managing director<span class="contact__role-cn" lang="zh">董事总经理</span></p>
      <address class="contact__details">
        Suite C410. Linden Court Business Centre<br>
        Maple East Rd Chaoyang District.<br>
        Beijing 100027<br>
        email: owen@brantwell.cn&nbsp; IM: owenbeijing<br>
        mobile: +86 13800427715
      </address>
      <address class="contact__details-cn" lang="zh">
        北京市朝阳区枫东路林登商务中心C410室 100027
      </address>
    </div>
  </section>
</body>
</html>
```